epoxy and decorative concrete information flyer

I need an informational flyer/pamphlet showcasing all of the services we offer. Summit Coatings offers a wide range of services. Epoxy flake systems for garages and commercial settings. stained concrete for patios and driveways. Stamped concrete with a large selection of designs. Cool decking for patios and around pools. <br/><br/>I'm looking for something proffessional and not too cluttered with info. <br/>Example: https://pics.bravolinkhub.net/q7RtLmZpW3xK9vBn2

Requirements
Must have
• Contact info phone 512-447-2816 summitcoatings.example info@summitcoatings.example
• A couple nice photos of what we do
• benefits of each service
• Epoxy is stain resistant, slip resistant, easy to clean and increases value of home.
• Stained and stamped concrete increases value of home and looks great.
• cool decking provides a much cooler surface for your feet in the summer months
Should not have
• color selections of epoxy
• I know my logo and website is red and black but I think that is too harsh of colors of a flyer. Please use more elegant and friendly colors.

```html
<!DOCTYPE html>
<html lang="en">
<head>
<meta charset="utf-8">
<title>Summit Coatings – Flooring Flyer</title>
<link href="https://fonts.googleapis.com/css2?family=Oswald:wght@400;500;600&family=Open+Sans:wght@400;600&display=swap" rel="stylesheet">
<style>
  :root {
    --ink: #27323f;
    --ink-deep: #1f2833;
    --accent: #d6a64f;
    --accent-dark: #b8893a;
    --silver: #d9d6cf;
    --white: #ffffff;
    --text-soft: #e9e6df;
  }
  * { margin: 0; padding: 0; box-sizing: border-box; }
  html, body { width: 966px; height: 1200px; overflow: hidden; background: #f2f2f2; }
  .flyer {
    position: relative; width: 966px; height: 1200px;
    background: var(--ink); overflow: hidden;
    font-family: "Open Sans", Arial, sans-serif; color: var(--white);
  }
  .shapes { position: absolute; inset: 0; }
  .tagline {
    position: absolute; top: 24px; left: 0; width: 100%; text-align: center;
    font-family: "Oswald", "Arial Narrow", sans-serif; font-weight: 400;
    font-size: 32px; line-height: 1.2;
  }
  .headline {
    position: absolute; top: 78px; left: 0; width: 100%; text-align: center;
    font-family: "Oswald", "Arial Narrow", sans-serif; font-weight: 500;
    font-size: 38px; line-height: 1.2; color: var(--accent); z-index: 2;
  }
  .brand-name {
    position: absolute; top: 628px; left: 0; width: 100%; text-align: center;
    font-family: "Oswald", "Arial Narrow", sans-serif; font-weight: 600;
    font-size: 38px; line-height: 1.05; letter-spacing: 4px; color: var(--white);
  }
  .benefits {
    position: absolute; top: 738px; left: 44px; width: 420px; list-style: none;
  }
  .services {
    position: absolute; top: 728px; left: 504px; width: 450px;
  }
  .services h2 {
    font-family: "Oswald", "Arial Narrow", sans-serif; font-weight: 500;
    font-size: 17px; line-height: 1.3; margin-bottom: 8px; white-space: nowrap;
  }
  .services ul { list-style: none; }
  .bullet-list li {
    position: relative; padding-left: 26px; color: var(--text-soft);
    font-size: 15px; line-height: 1.28; margin-bottom: 8px;
  }
  .services .bullet-list li { margin-bottom: 5px; font-size: 14px; }
  .bullet-list li::before {
    content: ""; position: absolute; left: 0; top: 3px;
    width: 14px; height: 14px; border-radius: 50%; background: var(--accent);
  }
  .bullet-list li::after {
    content: ""; position: absolute; left: 3.5px; top: 7px;
    width: 4px; height: 4px; border-right: 2px solid var(--white);
    border-top: 2px solid var(--white); transform: rotate(45deg);
  }
  .gallery { position: absolute; top: 884px; left: 41px; width: 881px; height: 168px; }
  .gallery-photo {
    position: absolute; top: 0; width: 263px; height: 168px;
    border: 2px solid #d7d7d7;
  }
  .photo-pool { left: 0; background: linear-gradient(180deg, #7c8f6e 0%, #4f9fd6 38%, #2e86c8 62%, #e8e4da 100%); }
  .photo-before-after { left: 307px; background: linear-gradient(135deg, #8aa0b3 0%, #b7c4cf 49.5%, #ffffff 49.5%, #ffffff 50.5%, #8f9396 50.5%, #6f7478 100%); }
  .photo-porch { left: 618px; background: linear-gradient(180deg, #f4f4f2 0%, #4d5e6e 30%, #56677a 70%, #9a9ea2 100%); }
  .photo-label {
    position: absolute; font-family: "Oswald", "Arial Narrow", sans-serif;
    font-size: 13px; color: var(--white);
  }
  .photo-label.before { top: 6px; left: 8px; }
  .photo-label.after { bottom: 6px; right: 8px; }
  .cta {
    position: absolute; top: 1120px; left: 0; width: 100%; text-align: center; z-index: 2;
    color: var(--ink-deep);
  }
  .cta-title {
    font-family: "Oswald", "Arial Narrow", sans-serif; font-weight: 500; font-size: 29px; line-height: 1.2;
  }
  .cta-contacts { font-size: 19px; margin-top: 2px; }
  .cta-contacts .sep { margin: 0 10px; }
</style>
</head>
<body>
<main class="flyer">
  <svg class="shapes" width="966" height="1200" viewBox="0 0 966 1200" aria-hidden="true">
    <path d="M0 70 Q483 260 966 70 L966 102 Q483 264 0 102 Z" fill="var(--accent)"/>
    <path d="M0 100 Q483 262 966 100 L966 112 Q483 274 0 112 Z" fill="var(--silver)"/>
    <path d="M0 598 Q483 492 966 598 L966 662 Q483 488 0 662 Z" fill="var(--accent)"/>
    <path d="M0 598 Q483 492 966 598 L966 610 Q483 504 0 610 Z" fill="var(--silver)"/>
    <path d="M0 1112 Q483 1076 966 1112 L966 1200 L0 1200 Z" fill="var(--silver)"/>
    <path d="M0 1122 Q483 1086 966 1122 L966 1200 L0 1200 Z" fill="var(--accent)"/>
  </svg>

  <svg class="shapes" width="966" height="1200" viewBox="0 0 966 1200" role="img" aria-label="Photo: sports car parked in a garage with a glossy epoxy floor, cabinets and a tool chest">
    <defs>
      <linearGradient id="hero-tone" x1="0" y1="0" x2="1" y2="1">
        <stop offset="0" stop-color="#6f7560"/>
        <stop offset="0.45" stop-color="#5b5d60"/>
        <stop offset="1" stop-color="#a9a6a0"/>
      </linearGradient>
    </defs>
    <path d="M0 110 Q483 272 966 110 L966 606 Q483 500 0 606 Z" fill="url(#hero-tone)"/>
  </svg>

  <p class="tagline">Summit Coatings provides the best flooring solutions on the market.</p>
  <h1 class="headline">MAKE YOUR GARAGE LOOK GREAT</h1>

  <div class="brand-name">SUMMIT<br>COATINGS</div>

  <ul class="benefits bullet-list">
    <li>Epoxy is stain resistant, slip resistant, easy to clean and increases value of home.</li>
    <li>Stained and stamped concrete increases value of home and looks great.</li>
    <li>Cool decking provides a much cooler surface for your feet in the summer months</li>
  </ul>

  <section class="services">
    <h2>SUMMIT COATINGS OFFERS A WIDE RANGE OF SERVICES.</h2>
    <ul class="bullet-list">
      <li>Epoxy flake systems for garages and commercial settings.</li>
      <li>Stained concrete for patios and driveways.</li>
      <li>Stamped concrete with a large selection of designs.</li>
      <li>Cool decking for patios and around pools.</li>
    </ul>
  </section>

  <div class="gallery">
    <div class="gallery-photo photo-pool" role="img" aria-label="Photo: pool surrounded by light cool decking"></div>
    <div class="gallery-photo photo-before-after" role="img" aria-label="Photo: before and after of a concrete floor given a flake epoxy finish">
      <span class="photo-label before">BEFORE</span>
      <span class="photo-label after">AFTER</span>
    </div>
    <div class="gallery-photo photo-porch" role="img" aria-label="Photo: front porch with a stained grey concrete floor"></div>
  </div>

  <footer class="cta">
    <div class="cta-title">CALL TODAY FOR YOUR FREE QUOTE</div>
    <div class="cta-contacts">summitcoatings.example<span class="sep">|</span>512-447-2816<span class="sep">|</span>info@summitcoatings.example</div>
  </footer>
</main>
</body>
</html>
```